TELURIN WEB DESIGN (please use the uploaded photos)

We are looking for a web design that captures the essence of Telurin: authenticity, connection with nature, and simplicity. We want the page to convey the story of our brand, from its cultural significance to its commitment to quality and authenticity. Additionally, we need to integrate Telurin's sub-brands, such as BOSRE, our line of healthy pecan nut snacks.

Design Objective:
We want our website to be more than just a product showcase: it should be a reflection of our brand identity and a platform that inspires our customers to connect with us on a deeper level.

Company Background:
Telurin is a company specializing in walnut production, hunting ranch management, and livestock. The name "Telurin" means "FOUR" in the PIMA dialect, in honor of the Pima communities that once inhabited the ranch. This historical and cultural connection is at the heart of our brand.

Audience Needs and Aspirations:
All our customers share deep emotional needs. They seek authenticity, honesty, and a happy, simple life. They want to reconnect with their natural state, dream, return to simplicity, and renew their hopes.

Brand Archetype:
Inspired by the archetypes of Greta, Tobias Wrenfield, and Innocent, we aim to reflect the need to be oneself, honesty, and authenticity in all aspects.

Brand Objective:
Our mission is to reconnect our customers with their natural state, offering high-quality products that simplify their lives and inspire them to dream and renew their hopes.

Key Design Elements:

Natural and earthy color palette reflecting our connection to nature.
Images and graphics depicting ranch life, walnut production, and the quality of our products.
Clean and easy-to-navigate design to reflect our philosophy of simplicity and honesty.
Seamless and clear integration of sub-brands, such as BOSRE.

Target Market(s)

Organic Women (30-50 years) committed to exercise and healthy diets. Hunters (40-60 years) with a deeply rooted conservative mindset. Prime Men (40-60 years) with high income, power, and status.

Coding

Coded - Design and coding required

Number of Pages Required

4 page

Other font styles liked:
• Brother 1816 Printed

Requirements
Must have
• Authenticity and Nature Connection: Reflect the brand's authenticity and connection to nature through design elements. Simplicity and Navigation: Keep the design clean and easy to navigate. Integration of Sub-brands: Seamlessly incorporate sub-brands like BOSRE into the design. Quality Imagery: Use high-quality visuals to showcase products and brand essence. Responsive Design: Ensure the website looks and functions well across different devices. Storytelling: Incorporate storytelling to convey the brand's history, values, and culture. Clear CTAs: Include clear calls-to-action to guide visitors towards desired actions.
Nice to have
• I have the telurinhq.com Domain, also I'm working on WIX

```html
<!DOCTYPE html>
<html lang="en">
<head>
<meta charset="utf-8">
<title>Bosre by Telurin</title>
<link href="https://fonts.googleapis.com/css2?family=Jost:wght@400;500;600&family=Lato:wght@400;700&display=swap" rel="stylesheet">
<style>
:root{
  --orange:#f26532;
  --orange-deep:#e0521f;
  --ink:#111111;
  --body:#2a2a2a;
  --cream:#fcf4f0;
  --white:#ffffff;
  --black:#000000;
}
*{margin:0;padding:0;box-sizing:border-box}
html,body{width:1200px;height:3424px;overflow:hidden;background:var(--white)}
body{position:relative;font-family:'Lato',sans-serif;color:var(--body)}
.abs{position:absolute}
.heading{font-family:'Jost',sans-serif;font-weight:500;color:var(--ink);letter-spacing:1px;text-transform:uppercase}
.btn{position:absolute;display:flex;align-items:center;justify-content:center;border-radius:40px;font-family:'Jost',sans-serif;font-size:19px;text-transform:uppercase;background:var(--orange);color:var(--white)}
.btn-outline{background:var(--white);color:var(--orange);border:2px solid var(--orange);font-size:15px}
.btn-light{background:var(--white);color:var(--orange)}
.center{left:0;width:1200px;text-align:center}

/* hero */
.hero{left:0;top:0;width:1200px;height:598px;background:linear-gradient(180deg,#7a6a2a 0%,#a6662a 22%,#8a4a22 45%,#4a3222 75%,#2c241c 100%)}
.hero::after{content:"";position:absolute;inset:0;background:radial-gradient(ellipse 260px 120px at 660px 130px,rgba(255,180,90,.55),transparent)}
.nav-link{top:49px;color:var(--white);font-family:'Jost',sans-serif;font-size:15px;font-weight:500;z-index:2}
.brand{left:500px;top:18px;width:200px;text-align:center;color:var(--white);font-family:'Jost',sans-serif;font-weight:500;font-size:56px;letter-spacing:3px;line-height:64px;z-index:2}
.brand small{position:absolute;left:130px;top:60px;font-size:9px;letter-spacing:.5px;line-height:12px}
.search{left:849px;top:47px;z-index:2}
.hero-title{top:192px;font-family:'Jost',sans-serif;font-size:60px;color:var(--white);letter-spacing:2px;z-index:2}
.hero-by{top:294px;font-family:'Jost',sans-serif;font-size:15px;font-weight:500;color:var(--white);z-index:2}
.hero-tag{top:340px;font-family:'Jost',sans-serif;font-size:20px;font-weight:500;color:var(--white);z-index:2}

/* about */
.about-back{left:153px;top:671px;width:383px;height:508px;background:var(--orange);border-radius:52% 48% 46% 54% / 36% 40% 60% 64%}
.about-photo{left:168px;top:674px;width:356px;height:498px;background:linear-gradient(160deg,#d9c3a6,#a8826a 55%,#5f4a3a);border-radius:52% 48% 44% 56% / 34% 38% 62% 66%}
.about-title{left:643px;top:672px;font-size:42px}
.about-text{left:616px;width:485px;font-size:15px;line-height:31px;color:var(--body)}

/* coming soon */
.soon{left:0;top:1243px;width:1200px;height:685px;background:var(--cream)}
.soon-title{top:1296px;font-size:42px}
.soon-sub{top:1372px;font-family:'Jost',sans-serif;font-size:15px;font-weight:500;color:var(--ink)}
.card-img{top:1429px;width:295px;height:239px;border-radius:6px}
.card{top:1631px;width:266px;height:219px;background:var(--white);border-radius:6px;box-shadow:0 4px 14px rgba(0,0,0,.06);text-align:center;padding:18px 14px 0}
.card h3{font-family:'Lato',sans-serif;font-weight:700;font-size:17px;color:var(--ink);line-height:26px;margin-bottom:6px}
.card p{font-size:13px;line-height:25px;color:var(--body)}

/* vision and mission */
.vm{left:0;top:1928px;width:1200px;height:429px}
.vm-title{font-size:42px;color:var(--white);top:2010px}
.vm-text{top:2092px;font-size:17px;line-height:34px;color:var(--white)}

/* subscribe */
.sub-title{top:2420px;font-size:42px}
.field{left:163px;top:2505px;width:874px;height:63px;border-radius:40px;background:var(--white);box-shadow:0 3px 14px rgba(0,0,0,.08);padding-left:39px;display:flex;align-items:center;font-family:'Jost',sans-serif;font-size:15px;font-weight:500;color:#333}

/* call to action */
.foot-bg{left:0;top:2864px;width:1200px;height:560px;background:var(--black)}
.cta{left:112px;top:2714px;width:978px;height:299px;border-radius:150px;background:linear-gradient(120deg,#e8602e,#f07038 50%,#e5592a)}
.cta-title{left:257px;top:2772px;font-size:44px;line-height:68px;color:var(--white);font-weight:600}
.cta-photo{left:803px;top:2727px;width:274px;height:274px;border-radius:50%;background:radial-gradient(circle at 45% 40%,#c9977a,#8a5a3e 60%,#5a3828)}

/* footer */
.foot-logo{left:112px;top:3092px;font-family:'Jost',sans-serif;font-size:48px;font-weight:400;color:var(--white);letter-spacing:2px;line-height:56px}
.social{top:3174px;width:32px;height:32px;border-radius:50%;background:var(--white)}
.foot-head{top:3094px;font-family:'Jost',sans-serif;font-size:20px;font-weight:600;color:var(--white)}
.foot-list{list-style:none;top:3138px}
.foot-list li{height:34.4px;font-family:'Jost',sans-serif;font-size:15px;color:var(--white);display:flex;align-items:center;gap:10px}
.contact-row{left:915px;display:flex;gap:12px;font-family:'Jost',sans-serif;font-size:16px;color:var(--white);line-height:27px}
.contact-row .ico{width:32px;height:32px;border-radius:50%;background:var(--white);flex:none;display:flex;align-items:center;justify-content:center}
.rule{left:112px;top:3344px;width:978px;height:1px;background:#555}
.copy{top:3378px;font-family:'Jost',sans-serif;font-size:15px;color:var(--white)}
</style>
</head>
<body>

<!-- hero -->
<div class="abs hero" role="img" aria-label="Cattle grazing in a ranch field at sunset"></div>
<div class="abs nav-link" style="left:110px">HOME</div>
<div class="abs nav-link" style="left:232px">BOSRE</div>
<div class="abs nav-link" style="left:352px">CONTACT</div>
<div class="abs brand">BOSRE<small>BY TELURIN</small></div>
<svg class="abs search" width="22" height="22" viewBox="0 0 22 22" fill="none" stroke="#fff" stroke-width="2"><circle cx="9" cy="9" r="7"/><path d="M14 14l6 6"/></svg>
<div class="btn" style="left:909px;top:36px;width:181px;height:45px;font-size:15px;font-weight:600">REQUEST A QUOTE</div>
<div class="abs center hero-title">WELCOME TO BOSRE</div>
<div class="abs center hero-by">BY TELURIN</div>
<div class="abs center hero-tag">WE BELIEVE IN THE POWER OF NATURE</div>
<div class="btn" style="left:517px;top:400px;width:167px;height:52px">START NOW</div>

<!-- about -->
<div class="abs about-back"></div>
<div class="abs about-photo" role="img" aria-label="Smiling woman holding a handful of pecans"></div>
<h2 class="abs heading about-title">ABOUT US</h2>
<p class="abs about-text" style="top:731px">We are a family-owned business dedicated to agriculture, which focuses on cultivating the Sonora region's pecan tree. Our goal is to create authentic products that harness the natural benefits of pecans. We believe in connecting with the land and using sustainable practices to grow pecan trees in the fertile soil of Sonora. This allows us to offer high-quality products that showcase the pure goodness of pecans.</p>
<p class="abs about-text" style="top:978px">At Telurin, we prioritize excellence and authenticity. Our products are carefully crafted to deliver a unique and satisfying experience. From our selection of fresh pecans to premium natural ingredients, we strive to provide the best to our customers.</p>
<div class="btn" style="left:618px;top:1115px;width:166px;height:51px">READ MORE</div>

<!-- coming soon -->
<div class="abs soon"></div>
<h2 class="abs heading center soon-title">COMING SOON</h2>
<div class="abs center soon-sub">AWAKE YOUR SENSES</div>

<div class="abs card-img" style="left:112px;background:linear-gradient(150deg,#6a4a32,#3a2a1e 60%,#2a1d14)" role="img" aria-label="Jar of pecan oil beside a bowl of pecans"></div>
<div class="abs card" style="left:126px"><h3>Pecan Oil</h3><p>Premium pecan oil, carefully extracted to retain its natural flavor and healthful properties, making it an ideal option for culinary purposes.</p></div>
<div class="btn btn-outline" style="left:192px;top:1794px;width:135px;height:40px">READ MORE</div>

<div class="abs card-img" style="left:452px;background:linear-gradient(150deg,#c89a72,#e4c7a4 55%,#b78a64)" role="img" aria-label="Hands chopping pecans on a wooden board"></div>
<div class="abs card" style="left:466px"><h3>Beauty Products Pecan Oil Based</h3><p>Unique beauty product line based on the benefits of pecan. Our products harness pecan oil's nourishing</p></div>
<div class="btn btn-outline" style="left:532px;top:1794px;width:135px;height:40px">READ MORE</div>

<div class="abs card-img" style="left:792px;background:linear-gradient(150deg,#e6e6e6,#cfcdcb 55%,#a7805e)" role="img" aria-label="Bowl of pecan flour with whole pecans"></div>
<div class="abs card" style="left:806px"><h3>Pecan Flour</h3><p>A versatile and nutritious option for all your baking needs.</p></div>
<div class="btn btn-outline" style="left:872px;top:1794px;width:135px;height:40px">READ MORE</div>

<!-- vision and mission -->
<svg class="abs vm" width="1200" height="429" viewBox="0 0 1200 429" role="img" aria-label="Dark pecan shells on the left and orange-tinted leaves on the right">
  <defs>
    <linearGradient id="darkPecan" x1="0" y1="0" x2="1" y2="1"><stop offset="0" stop-color="#3a2418"/><stop offset="1" stop-color="#1c130e"/></linearGradient>
    <linearGradient id="orangeLeaf" x1="0" y1="0" x2="1" y2="1"><stop offset="0" stop-color="#e8632f"/><stop offset="1" stop-color="#e3582a"/></linearGradient>
  </defs>
  <polygon points="0,0 637,0 550,429 0,429" fill="url(#darkPecan)"/>
  <polygon points="645,0 1200,0 1200,429 558,429" fill="#fff"/>
  <polygon points="653,0 1200,0 1200,429 566,429" fill="url(#orangeLeaf)"/>
</svg>
<h2 class="abs heading vm-title" style="left:136px">VISION</h2>
<p class="abs vm-text" style="left:112px;width:400px">To be a company that develops authentic products, services, and experiences that help reconnect with your natural state.</p>
<div class="btn" style="left:113px;top:2224px;width:166px;height:50px">READ MORE</div>
<h2 class="abs heading vm-title" style="left:700px;width:390px;text-align:right">MISSION</h2>
<p class="abs vm-text" style="left:690px;width:400px;text-align:right">Create innovative products and services that guide individuals toward rediscovering their true purpose.</p>
<div class="btn btn-light" style="left:922px;top:2224px;width:166px;height:50px">READ MORE</div>

<!-- subscribe -->
<h2 class="abs heading center sub-title">SUBSCRIBE FORM</h2>
<div class="abs field">Enter The Email</div>
<div class="btn" style="left:517px;top:2606px;width:167px;height:51px">JOIN NOW</div>

<!-- call to action -->
<div class="abs foot-bg"></div>
<div class="abs cta"></div>
<h2 class="abs heading cta-title">RECONNECT WITH<br>YOUR NATURAL STATE</h2>
<div class="btn btn-light" style="left:262px;top:2907px;width:166px;height:50px">CONTACT US</div>
<div class="abs cta-photo" role="img" aria-label="Portrait of a smiling woman in a knit sweater"></div>

<!-- footer -->
<div class="abs foot-logo">TELURIN</div>
<div class="abs social" style="left:112px"></div>
<div class="abs social" style="left:169px"></div>
<div class="abs social" style="left:227px"></div>
<div class="abs social" style="left:284px"></div>

<div class="abs foot-head" style="left:431px">QUICK LINKS</div>
<ul class="abs foot-list" style="left:431px">
  <li><svg width="13" height="12" viewBox="0 0 13 12" fill="#fff"><path d="M0 4.5h7V0l6 6-6 6V7.5H0z"/></svg>Home</li>
  <li><svg width="13" height="12" viewBox="0 0 13 12" fill="#fff"><path d="M0 4.5h7V0l6 6-6 6V7.5H0z"/></svg>About</li>
  <li><svg width="13" height="12" viewBox="0 0 13 12" fill="#fff"><path d="M0 4.5h7V0l6 6-6 6V7.5H0z"/></svg>Bosre</li>
  <li><svg width="13" height="12" viewBox="0 0 13 12" fill="#fff"><path d="M0 4.5h7V0l6 6-6 6V7.5H0z"/></svg>Contact Us</li>
</ul>

<div class="abs foot-head" style="left:680px">HELP LINKS</div>
<ul class="abs foot-list" style="left:680px">
  <li><svg width="13" height="12" viewBox="0 0 13 12" fill="#fff"><path d="M0 4.5h7V0l6 6-6 6V7.5H0z"/></svg>FAQ</li>
  <li><svg width="13" height="12" viewBox="0 0 13 12" fill="#fff"><path d="M0 4.5h7V0l6 6-6 6V7.5H0z"/></svg>Terms of use</li>
  <li><svg width="13" height="12" viewBox="0 0 13 12" fill="#fff"><path d="M0 4.5h7V0l6 6-6 6V7.5H0z"/></svg>Privacy Policy</li>
  <li><svg width="13" height="12" viewBox="0 0 13 12" fill="#fff"><path d="M0 4.5h7V0l6 6-6 6V7.5H0z"/></svg>Support Links</li>
  <li><svg width="13" height="12" viewBox="0 0 13 12" fill="#fff"><path d="M0 4.5h7V0l6 6-6 6V7.5H0z"/></svg>Conditions</li>
</ul>

<div class="abs foot-head" style="left:915px">CONTACT US</div>
<div class="abs contact-row" style="top:3140px">
  <span class="ico"><svg width="14" height="18" viewBox="0 0 14 18"><path d="M7 0a7 7 0 0 0-7 7c0 5 7 11 7 11s7-6 7-11a7 7 0 0 0-7-7z" fill="#000"/><circle cx="7" cy="7" r="2.6" fill="#fff"/></svg></span>
  <span>Telurin Ranch<br>United States</span>
</div>
<div class="abs contact-row" style="top:3207px">
  <span class="ico"><svg width="16" height="16" viewBox="0 0 16 16"><path d="M3 1l3 3-2 2c1 2 3 4 6 6l2-2 3 3-2 2C7 15 1 9 1 3z" fill="#000"/></svg></span>
  <span style="line-height:32px">+1 888 888 8888</span>
</div>
<div class="abs contact-row" style="top:3258px">
  <span class="ico"><svg width="16" height="12" viewBox="0 0 16 12"><rect width="16" height="12" rx="1.5" fill="#000"/><path d="M1 1l7 5 7-5" stroke="#fff" stroke-width="1.4" fill="none"/></svg></span>
  <span style="line-height:32px">info@telurinhq.com</span>
</div>

<div class="abs rule"></div>
<div class="abs center copy">Copyrights@2024.Bosre.All Rights Reserved</div>

</body>
</html>
```